Concert festival poster

Poster invitation for 40th party designed to look like a concert festival. Using the samples attached as a guide, looking for a colorful, creative and eye catching invite.
The event will be held over a weekend at a farm, with music food, friends and drinks.

Target Market(s)

Party guests, friends and family

Industry/Entity Type

Festival

Colors

Designer to choose colors to be used in the design.

Requirements
Must have
• Brellafest- Mark Telford's 40th festival
• Event date- 5-7th October 2018. Main event 6th October 2018 from 3pm-late
• Come anytime over the weekend- food, drinks and fun provided.
• Address is 412 Stony Creek Lane, Marulan NSW
• All welcome, including children
• Bring your own tent or let us know and we can arrange glamping tent set-up on site
• RSVP by 1 May 2018 to Kate at kate.anne.telford@mailbox-demo.com or Mark at mtelford@vantor-telford.com.au
• Will add extra information on event at later stage- see below for editable section.
Nice to have
• Editable section to add details, preferable at bottom of poster.

```html
<!DOCTYPE html>
<html lang="en">
<head>
<meta charset="utf-8">
<title>Brellafest – Mark Telford's 40th Festival</title>
<link rel="stylesheet" href="https://fonts.googleapis.com/css2?family=Bungee&family=Bungee+Inline&family=Didact+Gothic&family=Oswald:wght@500;600&family=Lobster&display=swap">
<style>
  :root {
    --navy-deep: #0a1524;
    --navy: #14263d;
    --navy-light: #22395a;
    --blue: #1fa3e8;
    --blue-bright: #35b8f5;
    --white: #f4f7fb;
    --muted: #c9d4e3;
    --silver-1: #e8eef6;
    --silver-2: #8fa3bf;
    --gold: #e6c23a;
  }
  * { margin: 0; padding: 0; box-sizing: border-box; }
  html, body { width: 898px; height: 1200px; overflow: hidden; background: var(--navy-deep); }
  .poster {
    position: relative;
    width: 898px;
    height: 1200px;
    overflow: hidden;
    background: radial-gradient(ellipse at 60% 40%, var(--navy-light) 0%, var(--navy) 45%, var(--navy-deep) 100%);
    font-family: "Didact Gothic", sans-serif;
    color: var(--white);
  }
  .guitar-art {
    position: absolute; left: 0; top: 0; width: 235px; height: 1200px;
    background: linear-gradient(180deg, rgba(60,110,160,0.25) 0%, rgba(40,150,210,0.45) 55%, rgba(70,190,240,0.6) 100%);
  }
  .centered { position: absolute; left: 230px; width: 650px; text-align: center; white-space: nowrap; }
  .host { top: 24px; font-size: 21px; line-height: 1.2; letter-spacing: 2px; color: var(--blue); }
  .age { top: 52px; font-family: "Bungee Inline", sans-serif; font-size: 88px; line-height: 1; color: var(--blue); letter-spacing: -2px; }
  .festival-word { top: 150px; font-size: 19px; line-height: 1.2; letter-spacing: 17px; font-weight: bold; padding-left: 17px; }
  .title { font-family: "Bungee", sans-serif; line-height: 1;
    background: linear-gradient(160deg, var(--silver-1) 0%, var(--silver-2) 50%, var(--silver-1) 100%);
    -webkit-background-clip: text; background-clip: text; color: transparent;
    filter: drop-shadow(3px 4px 2px rgba(0,0,0,0.6)); }
  .title-top { top: 215px; font-size: 124px; }
  .title-bottom { top: 385px; font-size: 170px; }

  .date-block { position: absolute; }
  .date-event { left: 300px; top: 614px; width: 190px; }
  .date-main { left: 650px; top: 608px; width: 180px; text-align: center; }
  .date-label { font-size: 22px; line-height: 26px; letter-spacing: 0.5px; white-space: nowrap; }
  .date-day { font-family: "Oswald", sans-serif; font-weight: 600; font-size: 62px; line-height: 62px; color: var(--blue-bright); white-space: nowrap; }
  .date-month { font-family: "Oswald", sans-serif; font-weight: 500; font-size: 27px; line-height: 30px; white-space: nowrap; }
  .date-time { font-size: 18px; line-height: 22px; color: var(--muted); white-space: nowrap; }
  .violin-art { position: absolute; left: 515px; top: 616px; width: 76px; height: 104px; border-radius: 38px 38px 28px 28px;
    background: linear-gradient(180deg, rgba(255,255,255,0.5), rgba(255,255,255,0.2)); }

  .address { top: 764px; font-size: 29px; line-height: 36px; }
  .anytime { top: 812px; font-size: 21px; line-height: 26px; letter-spacing: 0.5px; }
  .offer { position: absolute; top: 858px; width: 200px; text-align: center; }
  .offer-food { left: 225px; } .offer-drinks { left: 467px; } .offer-fun { left: 701px; }
  .offer svg { display: block; margin: 0 auto 8px; }
  .offer-label { font-family: "Bungee Inline", sans-serif; font-size: 26px; line-height: 1.1; color: var(--blue); }
  .divider { position: absolute; top: 870px; width: 1px; height: 60px; background: var(--blue); opacity: 0.6; }
  .welcome { top: 968px; font-family: "Lobster", cursive; font-size: 42px; line-height: 1.2; }
  .tent { top: 1027px; font-size: 19px; line-height: 1.28; }
  .rule { position: absolute; left: 513px; top: 1094px; width: 76px; height: 2px; background: var(--gold); }
  .rsvp { top: 1110px; font-size: 20px; line-height: 1.38; }
  .rsvp .accent { color: var(--blue-bright); }
  .rsvp .deadline { font-weight: bold; letter-spacing: 1px; }
</style>
</head>
<body>
<main class="poster">
  <div class="guitar-art" role="img" aria-label="Guitar shape made of music notes over faint sketched festival doodles"></div>

  <p class="centered host">MARK TELFORD'S</p>
  <h2 class="centered age">40TH</h2>
  <p class="centered festival-word">FESTIVAL</p>

  <h1 class="centered title title-top">BRELLA</h1>
  <div class="centered title title-bottom" aria-hidden="true">FEST</div>

  <div class="date-block date-event">
    <p class="date-label">EVENT DATE</p>
    <p class="date-day">5-7 TH</p>
    <p class="date-month">OCTOBER 2018</p>
  </div>
  <div class="violin-art" role="img" aria-label="Violin silhouette with ornamental flourishes"></div>
  <div class="date-block date-main">
    <p class="date-label">MAIN EVENT</p>
    <p class="date-day">6TH</p>
    <p class="date-month">OCTOBER 2018</p>
    <p class="date-time">FROM 3PM-LATE</p>
  </div>

  <p class="centered address">412 Stony Creek Lane, Marulan NSW</p>
  <p class="centered anytime">Come anytime over the weekend</p>

  <div class="offer offer-food">
    <svg width="50" height="40" viewBox="0 0 50 40" fill="#fff"><circle cx="25" cy="6" r="3"/><path d="M5 30a20 20 0 0 1 40 0z"/><rect x="2" y="32" width="46" height="4" rx="2"/></svg>
    <p class="offer-label">FOOD</p>
  </div>
  <div class="divider" style="left:438px"></div>
  <div class="offer offer-drinks">
    <svg width="50" height="40" viewBox="0 0 50 40" fill="none" stroke="#fff" stroke-width="2.5"><path d="M10 4h30L25 20z" fill="#fff"/><path d="M25 20v15M16 37h18"/><circle cx="36" cy="5" r="3" fill="#fff"/></svg>
    <p class="offer-label">DRINKS</p>
  </div>
  <div class="divider" style="left:702px"></div>
  <div class="offer offer-fun">
    <svg width="50" height="40" viewBox="0 0 50 40" fill="#fff"><path d="M6 6l22 8-14 14z"/><circle cx="34" cy="20" r="2.5"/><circle cx="40" cy="12" r="2"/><circle cx="30" cy="30" r="2"/><circle cx="42" cy="28" r="2.5"/></svg>
    <p class="offer-label">FUN</p>
  </div>

  <p class="centered welcome">All Welcome, Including Children</p>
  <p class="centered tent">Bring your own tent or let us know and we can arrange<br>glamping tent set-up on site</p>
  <div class="rule"></div>
  <p class="centered rsvp">RSVP by <span class="accent deadline">1 MAY 2018</span> to<br>Kate at <span class="accent">kate.anne.telford@mailbox-demo.com</span> or<br>Mark at <span class="accent">mtelford@vantor-telford.com.au</span></p>
</main>
</body>
</html>
```